Veterinary Business cards

Redesign Business Card

Information needed on Card:
Hours: Mon-Fri: 4pm -10PM; Sat- Sun- 10 AM- 5PM
Help@bayfernvet.com
www.bayfernvet.com
555-718-2946
4173 SE 19th Ave. okc, ok 73958
*No appointment necessary*

Optional:
Our tag line is "We're here when you need us" - If it fits on the cards.

```html
<!DOCTYPE html>
<html lang="en">
<head>
<meta charset="utf-8">
<title>Bayfern Urgent Care – Business Card</title>
<link href="https://fonts.googleapis.com/css2?family=Montserrat:ital,wght@0,400;0,500;0,700;1,500&display=swap" rel="stylesheet">
<style>
  :root {
    --page: #fafafa;
    --navy: #1a3a66;
    --orange: #d67a2a;
    --white: #ffffff;
    --shadow: rgba(0, 0, 0, 0.18);
  }
  * { box-sizing: border-box; margin: 0; padding: 0; }
  html, body {
    width: 800px;
    height: 1200px;
    overflow: hidden;
    background: var(--page);
    font-family: "Montserrat", Arial, sans-serif;
    color: var(--white);
  }
  .sheet {
    width: 800px;
    height: 1200px;
    display: flex;
    flex-direction: column;
    align-items: center;
    justify-content: center;
    gap: 40px;
  }
  .card {
    position: relative;
    width: 640px;
    height: 366px;
    background: var(--navy);
    box-shadow: 0 1px 3px var(--shadow);
    overflow: hidden;
  }

  /* Front */
  .brand-name {
    display: flex;
    align-items: center;
    gap: 10px;
    font-weight: 500;
    text-transform: uppercase;
    letter-spacing: 0.08em;
    color: var(--white);
  }
  .brand-dot {
    width: 14px;
    height: 14px;
    border-radius: 50%;
    background: var(--orange);
    flex: none;
  }
  .card-front .brand-name {
    position: absolute;
    left: 42px;
    top: 64px;
    font-size: 27px;
  }
  .contact-list {
    position: absolute;
    left: 38px;
    top: 176px;
    list-style: none;
    font-size: 17px;
    line-height: 1.25;
  }
  .contact-item {
    display: flex;
    align-items: flex-start;
    gap: 10px;
    margin-bottom: 8px;
  }
  .contact-icon {
    width: 13px;
    height: 13px;
    margin-top: 4px;
    flex: none;
  }
  .paw-area {
    position: absolute;
    right: 0;
    top: 0;
    width: 274px;
    height: 366px;
  }

  /* Back */
  .card-back {
    display: flex;
    flex-direction: column;
    align-items: center;
    text-align: center;
  }
  .walk-in-note {
    margin-top: 62px;
    font-size: 15px;
    font-weight: 700;
    letter-spacing: 0.22em;
  }
  .card-back .brand-name {
    margin-top: 56px;
    font-size: 32px;
  }
  .website {
    margin-top: 30px;
    font-size: 16px;
    font-weight: 400;
  }
  .tagline {
    margin-top: 36px;
    font-size: 20px;
    font-weight: 500;
    font-style: italic;
    color: var(--orange);
  }
</style>
</head>
<body>
<main class="sheet">

  <section class="card card-front">
    <div class="brand-name"><span class="brand-dot"></span>Bayfern Urgent Care</div>

    <ul class="contact-list">
      <li class="contact-item">
        <svg class="contact-icon" viewBox="0 0 16 16" aria-hidden="true">
          <path fill="var(--orange)" d="M4 1l3 3-2 2c1 2 3 4 5 5l2-2 3 3-2 3C7 15 1 9 1 3z"/>
        </svg>
        <span>555-718-2946</span>
      </li>
      <li class="contact-item">
        <svg class="contact-icon" viewBox="0 0 16 16" aria-hidden="true">
          <path fill="var(--orange)" d="M8 0a5.5 5.5 0 0 0-5.5 5.5C2.5 10 8 16 8 16s5.5-6 5.5-10.5A5.5 5.5 0 0 0 8 0zm0 8a2.5 2.5 0 1 1 0-5 2.5 2.5 0 0 1 0 5z"/>
        </svg>
        <span>4173 SE 19th Ave. OKC, OK 73958</span>
      </li>
      <li class="contact-item">
        <svg class="contact-icon" viewBox="0 0 16 16" aria-hidden="true">
          <rect x="0" y="3" width="16" height="10" fill="var(--orange)"/>
          <path d="M0 3l8 6 8-6" fill="none" stroke="var(--navy)" stroke-width="1.5"/>
        </svg>
        <span>Help@bayfernvet.com</span>
      </li>
      <li class="contact-item">
        <svg class="contact-icon" viewBox="0 0 16 16" aria-hidden="true">
          <rect x="1" y="3" width="12" height="11" fill="none" stroke="var(--orange)" stroke-width="1.5"/>
          <line x1="1" y1="6" x2="13" y2="6" stroke="var(--orange)" stroke-width="1.5"/>
          <circle cx="12" cy="12" r="3.3" fill="var(--navy)" stroke="var(--orange)" stroke-width="1.3"/>
        </svg>
        <span>Monday to Friday: 4pm to 10PM<br>Saturday and Sundays: 10 AM to 5PM</span>
      </li>
    </ul>

    <svg class="paw-area" viewBox="0 0 274 366" role="img" aria-label="Large decorative paw print in orange">
      <defs>
        <radialGradient id="pawGlow" cx="0.7" cy="0.55" r="0.7">
          <stop offset="0" stop-color="var(--orange)"/>
          <stop offset="1" stop-color="var(--orange)" stop-opacity="0.85"/>
        </radialGradient>
      </defs>
      <circle cx="230" cy="190" r="175" fill="url(#pawGlow)"/>
    </svg>
  </section>

  <section class="card card-back">
    <p class="walk-in-note">NO APPOINTMENT NECESSARY</p>
    <div class="brand-name"><span class="brand-dot"></span>Bayfern Urgent Care</div>
    <p class="website">bayfernvet.com</p>
    <p class="tagline">WE'RE HERE WHEN YOU NEED US</p>
  </section>

</main>
</body>
</html>
```